International Property Consultancy

Brief Overview:

I need a dynamic and well designed website that is easy to use and understand. It has to be unique and different to generic templates that most websites seem to be these days. PLEASE NO GENERIC TEMPLATES FROM THE INTERNET.

Our business has 10 years experience working on struggling international developments that we then work in-house for to turn around and brings bout success. We stay within a project often for long periods of time until success is achieved. We are unique in our approach and completely different to the standard routes to market for many developments. The site is for developers to see what we have done in regards to previous projects, as such we want to incorporate video into this site with a strong design aesthetic. There will be videos of the past projects we have worked on, which will act as case studies.

I like very simple but punchy websites, that people can navigate and understand very easily. Also a big fan of unique and well thought out design aesthetic.

Initial Site layout thoughts:

1) Homepage:
2) About Us
3) What we've done / Work
This part has the projects we have worked on (France, Portugal, London, Morocco). Each one will have some video content and photo images, but also would be good to have a succinct way to mention what we did and the successes in a clever and punchy way.

4) Contact Us

* This is just a guideline. Would be open to input and creative direction on your own part.

*More details and websites we like can be seen in the brief doc attached.

PLEASE VIEW THE WIREFRAME WORD DOC ATTACHED.

Here there are also some more examples to help:

Here are just a few examples of websites and what I like about them:

- www.velmoro.com (clean, nice geometric design aesthetic, good animation when loading and changing pages well thought out all though also coulee be considered a bit dull and basic after the initial homepage slide)
- https://www.farbridgehub.net (Clean site, quite clinical, lacks video content and doesn't engage greatly).
- https://ruskotile.com (minimal, and like how it mixes the design aesthetic more with video and photo content)

- https://www.amberquillworks.com (like the layout of this and how it displays the projects and work section)

- https://brisk.com (Good use of video content)

- https://loomfield.studio (minimal to the point and mixes design with video and animation etc...)

Here is another couple of cool websites that may help give you some direction: https://halvenquay.com www.brisk.com

Hi there, One of the things I thought would be good on the homepage is to add the logo with a 'digital landscape' before flicking down into a slide with video content of the projects... Just an idea but have posted some pics in the brief. We would get this animated for the site. But if you have better ideas, please do run with them. Thanks,

Target Market(s)

Property developers

Number of Pages Required

4 page

Font styles to use
Other font styles liked:
• Read brief

Requirements
Must have
• Needs to be clean, dynamic and easy to follow on desktop and mobile. We will use it as a kind of portfolio website so will need to embed video of past projects we have worked on.

Read brief in docs.
Nice to have
• Clean
Should not have
• Not be another generic template website.
Not have random property stock photos. (We are not a property agency).

```html
<!DOCTYPE html>
<html lang="en">
<head>
<meta charset="utf-8">
<title>Calvenor — International Property Developments</title>
<link rel="stylesheet" href="https://fonts.googleapis.com/css2?family=Exo+2:wght@500;600;700&family=Roboto:wght@400&display=swap">
<style>
  :root {
    --navy: #22304f;
    --ink: #333640;
    --body: #4a4d57;
    --muted: #a9adb8;
    --white: #ffffff;
    --glow-orange: #f0a64a;
    --glow-yellow: #f3d83c;
    --rule: #c9ccd3;
    --mist: #f1f3f8;
    --mist-deep: #e6eaf3;
  }
  * { box-sizing: border-box; margin: 0; padding: 0; }
  html, body { width: 1138px; height: 1200px; overflow: hidden; background: var(--white); }
  body { position: relative; font-family: "Roboto", sans-serif; color: var(--body); }

  .site-header { position: absolute; left: 0; top: 0; width: 1138px; height: 89px; background: var(--white); }
  .brand { position: absolute; left: 135px; top: 16px; font-family: "Exo 2", sans-serif; font-weight: 600; font-size: 48px; color: var(--navy); letter-spacing: 0.5px; line-height: 1; }
  .main-nav a { position: absolute; top: 33px; font-family: "Exo 2", sans-serif; font-weight: 600; font-size: 20px; color: var(--navy); text-decoration: none; line-height: 1; }
  .search-btn { position: absolute; left: 961px; top: 25px; width: 38px; height: 38px; border: 2px solid var(--navy); border-radius: 50%; }
  .search-btn svg { position: absolute; left: 10px; top: 10px; }

  .hero { position: absolute; left: 0; top: 89px; width: 1138px; height: 618px; background: var(--navy); overflow: hidden; }
  .hero-landscape { position: absolute; left: 0; top: 180px; width: 1138px; height: 438px;
    background:
      radial-gradient(ellipse 260px 140px at 860px 230px, rgba(243,216,60,0.55), transparent 70%),
      radial-gradient(ellipse 520px 260px at 720px 230px, rgba(240,166,74,0.45), transparent 75%),
      radial-gradient(ellipse 420px 160px at 200px 280px, rgba(240,166,74,0.3), transparent 75%); }
  .hero-title { position: absolute; left: 136px; top: 92px; font-family: "Exo 2", sans-serif; font-weight: 700; font-size: 72px; line-height: 1; color: var(--white); letter-spacing: -0.5px; }
  .hero-sub { position: absolute; left: 137px; top: 167px; font-family: "Exo 2", sans-serif; font-weight: 600; font-size: 26px; color: var(--white); line-height: 1; }
  .play { position: absolute; left: 512px; top: 283px; }

  .cta-title { position: absolute; left: 136px; top: 745px; width: 500px; font-family: "Exo 2", sans-serif; font-weight: 600; font-size: 33px; line-height: 38px; color: var(--ink); }
  .cta-button { position: absolute; left: 807px; top: 750px; width: 194px; height: 56px; background: var(--navy); color: var(--white); font-family: "Exo 2", sans-serif; font-weight: 600; font-size: 17px; display: flex; align-items: center; justify-content: center; text-decoration: none; }
  .divider { position: absolute; left: 137px; top: 866px; width: 864px; height: 1px; background: var(--rule); }

  .footer-backdrop { position: absolute; left: 0; top: 930px; width: 1138px; height: 270px;
    background: linear-gradient(180deg, rgba(241,243,248,0) 0%, var(--mist) 45%, var(--mist-deep) 100%); }
  .footer-brand { position: absolute; left: 137px; top: 900px; font-family: "Exo 2", sans-serif; font-weight: 500; font-size: 40px; color: var(--muted); line-height: 1; }
  .footer-about { position: absolute; left: 135px; top: 966px; width: 215px; font-size: 11.5px; line-height: 21px; }
  .social { position: absolute; left: 136px; top: 1056px; display: flex; gap: 12px; }
  .social span { width: 14px; height: 14px; border-radius: 3px; background: var(--muted); display: block; }
  .footer-col { position: absolute; top: 911px; }
  .footer-col h4 { font-family: "Exo 2", sans-serif; font-weight: 500; font-size: 13px; letter-spacing: 0.6px; color: var(--body); margin-bottom: 24px; }
  .footer-col li { list-style: none; font-size: 11.5px; line-height: 21.2px; }
  .footer-col.contact h4 { margin-bottom: 20px; }
  .copyright { position: absolute; left: 0; top: 1152px; width: 1155px; text-align: center; font-size: 12.5px; letter-spacing: 0.4px; color: var(--body); }
</style>
</head>
<body>
  <header class="site-header">
    <div class="brand">calvenor.</div>
    <nav class="main-nav">
      <a href="#" style="left:556px">Home</a>
      <a href="#" style="left:640px">About Us</a>
      <a href="#" style="left:753px">Work</a>
      <a href="#" style="left:834px">Contact Us</a>
    </nav>
    <div class="search-btn">
      <svg width="14" height="14" viewBox="0 0 14 14"><circle cx="6" cy="6" r="4.2" fill="none" stroke="#22304f" stroke-width="2"/><line x1="9" y1="9" x2="12.5" y2="12.5" stroke="#22304f" stroke-width="2" stroke-linecap="round"/></svg>
    </div>
  </header>

  <section class="hero">
    <div class="hero-landscape" role="img" aria-label="Glowing orange and yellow wireframe digital landscape rolling across the hero"></div>
    <h1 class="hero-title">We are Calvenor</h1>
    <p class="hero-sub">We fulfill international property developments</p>
    <svg class="play" width="114" height="114" viewBox="0 0 114 114" aria-label="Play video">
      <circle cx="57" cy="57" r="55" fill="none" stroke="#ffffff" stroke-width="3"/>
      <circle cx="57" cy="57" r="44" fill="rgba(34,48,79,0.35)" stroke="rgba(255,255,255,0.35)" stroke-width="1.5"/>
      <path d="M41 36 L75 57 L41 78 Z" fill="#ffffff"/>
    </svg>
  </section>

  <h2 class="cta-title">Sed ut peomnis iste natus volu ptatem accusantium dolor</h2>
  <a class="cta-button" href="#">View Our Projects</a>
  <div class="divider"></div>

  <div class="footer-backdrop" role="img" aria-label="Soft pale landscape backdrop behind the footer"></div>

  <div class="footer-brand">calvenor.</div>
  <p class="footer-about">Sed ut perspiciatis unde omnis iste natus error sit voluptatem accusantium doloremque laudantium.</p>
  <div class="social" aria-label="Social links"><span></span><span></span><span></span><span></span><span></span></div>

  <div class="footer-col" style="left:432px">
    <h4>PROJECTS</h4>
    <ul><li>Sed ut perspiciatis</li><li>Gmnis iste natus</li><li>Rsit voluptatem</li><li>Accusantium</li><li>Holoremque</li></ul>
  </div>
  <div class="footer-col" style="left:622px">
    <h4>LINKS</h4>
    <ul><li>Sed ut pespic</li><li>Gmnis istenatus</li><li>Rsit voluptatem</li><li>Accusatium</li><li>Holoremue</li></ul>
  </div>
  <div class="footer-col contact" style="left:828px">
    <h4>CONTACT</h4>
    <ul><li>Sed ut perspdummu 25 iciatis</li><li>Gmnis iste natus 125</li><li>Phone: 163 418 7720</li><li>Email:hello@calvenor-mail.com</li></ul>
  </div>

  <p class="copyright">© 2020 CALVENOR. ALL RIGHTS RESERVED. PRIVACY POLICY, TERMS AND CONDITIONS</p>
</body>
</html>
```